www.telvoqa.io - DESIGN ONLY

I needs designs for an application that will allow users to email/sms/tweet messages that will be picked up by the system and displayed in s simmilar mannor to an email inbox.

I actually need 3-4 pages designs, in this priority order:

- Inbox (list)
- Inbox display message details of a single inbox item.
- Login/register

Additionally, it would be nice (but not 100% necessarily) if I could get a sample form page, that I can taylor for the alternative sign up message sources. But I can probably get this form the registration page.

More Info
-

What I am looking to build is an application that allows users to email (and later IM, text and tweet) messages all that will be retrieved by the system. Giving a central point to view/categorize and share this information. I guess you could think of it a bit like and email inbox that only I can post to mixed with pinnacrux (online bookmarks).

Ok, so the design will need a homepage explaining what the app does, with the ability to register/login etc, please just provide designs for a login/regitration screen I will add the description of what the app does.

It is the design of the inbox area is where I mostly want you guys to concentrate on. So when the user first registers, and have yet to see any messages in there inbox, they should see text saying something like:

"Well that was easy, now simply send your emails to xxx@telvoqa.io and it will show up here in your inbox"

Once the user sends an email to this account, it will will appear in a list (showing only the title, in a very similar to the way that email inbox works). The additional information that I want to show in this list are:

- Source: Email, Vondel, chirpnest, SMS etc... so little icons for each would be nice.

- Date received: Will say "5mins ago" or "5 hours ago" etc, until its over a day old then it will say "5th Nov at 12:20" or similar

- Tags: When messages are sent you can "tag" them using chirpnest style hash tags. A sample message might be "Buy some milk #urgent"

- Favorite/Star: A mechanism to favorite or star a message for priority view.

- Links: I will parse the messages and look for links in the messages. I want to display the number of links found in the message, and display a link, which when clicked will display a panel at the cursor with all the links (and a screenshot of the website found).

- Message Info (In list): The system will be a little smart here, as I want to display different types of messages in different ways i.e:

1) If the message received is an email with just a link in there then I will just display a small thumbnail and a the link

2) If the message is a tweet, then I would display the whole thing in speech marks "

3) If the message is an email with a message body, just display the title until clicked on

So, if a message isn't displayed fully already, then clicking the message should display it in full (standard email behavior).

Other things that should be on this page are:

- A tag list of tags (or tag cloud), which when clicked will filter the messages (messages can be dragged here to tag)
- A Trash can (to drag the messages on to delete)
- A search bar for full text search
- A hints bubble/pane/whatever where I can tell users how to tag messages etc
- Links to register other sources (chirpnest account, mobile number, etc).

Other pages:
- Registration/Login
- Sample form for Signingup to register other message source i.e. chirpnest, Vondel chat, sms. I basically just need an example form page and I can amend as required.

Design:

I would like the design to be quite "chunky" and I want it to be a fluid, full screen layout.

Also, the page should fill the screen and not be vertically scrolling. The only part that should scroll is the section where the messages are listed/shown, so that dragging of messages, from the list to the trash can/tags is always available.

Here are some examples of the messages layouts that I like:

- zarimo post (like the chunkiness of the design)
- http://www.peoplewallo.net/ (Messages on people walls)
- http://tunekelpi.com/ (When playing a song the bottom of the screen shows the info about the current playing song in a very compact way, I like this a lot)
- http://plonq.com/
- http://querymantle.com/
Updates

Please forget the name "brixalune.com" it's a terrible name. I'm still looking for suitable domain names, so just leave a place holder for the logo, or add a generic looking thing there. 

The name of the domain I will use is no longer brixalune.com instead it will be www.telvoqa.io or www.telvoqanet.com.

Hey all, 

I have yet to receive a design, do you guys need any more information to begin the process?

Dervan. 

All I want for Christmas is a design or two. 

Seriously though, is there anything I can do to get this process rolling? 

Budget

I didn't think the budget was too low for this kind of project (essentially a few page designs), but if you disagree then I will consider raising the budget.

Requirements

Are they unclear?

Patience

Do I just need to be more patient? I just don't want to receive all designs on the last day then have to choose a winner without having time for amends. 

Questions comment, anything welcome. 

Cheers, Dervan. 

Design budget increased due to lack of submissions (now £425/~$670). 

Industry/Entity Type

Build

Requirements
Must have
• - Inbox Design (list)
- Inbox display message Design i.e. details of a single inbox item.
- Login/register Design
Nice to have
• - Sample form page for registering alternative messages sources like Vondel chats, SMS's etc.

```html
<!DOCTYPE html>
<html lang="en">
<head>
<meta charset="utf-8">
<title>telvoqa.io – Inbox</title>
<link href="https://fonts.googleapis.com/css2?family=PT+Sans:ital,wght@0,400;0,700;1,700&display=swap" rel="stylesheet">
<style>
:root{
  --ink:#1d1d1d;
  --muted:#555;
  --line:#d4d4d4;
  --head-dark:#0f1418;
  --blue:#1f8fd3;
  --blue-light:#4fb4ea;
  --blue-dark:#1476b6;
  --link:#1a6fa8;
  --row:#ffffff;
  --row-alt:#f0f0f0;
  --preview-head:#d3dde3;
  --tag-bg:#f3f3f3;
  --white:#fff;
}
*{box-sizing:border-box;margin:0;padding:0}
html,body{width:1200px;height:770px;overflow:hidden}
body{font-family:"PT Sans",Arial,sans-serif;color:var(--ink);background:var(--white);position:relative;font-size:13px}
.abs{position:absolute}

/* top bar */
.topbar{left:0;top:0;width:1200px;height:50px;background:linear-gradient(#2a3640,var(--head-dark))}
.brand{left:16px;top:8px;display:flex;align-items:center;gap:10px}
.brand-dot{width:30px;height:30px;border-radius:50%;background:#3b4a55}
.brand-name{color:var(--white);font-weight:700;font-size:29px;line-height:1}
.social{left:243px;top:15px;display:flex;gap:5px}
.social span{width:19px;height:19px;background:var(--white);border-radius:2px;display:block}
.nav{right:144px;top:16px;display:flex;color:var(--white);font-weight:700;font-size:13px}
.nav a{color:inherit;text-decoration:none;padding:0 8px;border-left:1px solid #556}
.nav a:first-child{border-left:0}
.user{left:1076px;top:10px;display:flex;align-items:center;gap:12px;color:var(--white);font-weight:700;font-size:13px}
.avatar{width:30px;height:30px;border:2px solid #ddd;background:linear-gradient(#7da2c8,#2b4f77)}

/* toolbar */
.toolbar{left:0;top:50px;width:1200px;height:53px;background:linear-gradient(var(--blue-light),var(--blue-dark))}
.tool{top:9px;width:66px;height:32px;border-radius:3px;background:linear-gradient(#fff,#dfe3e6);border:1px solid #0d5d90;display:flex;align-items:center;justify-content:center}
.search{left:908px;top:10px;width:276px;height:32px;border-radius:16px;background:var(--white);border:1px solid #0d5d90;box-shadow:inset 0 1px 3px rgba(0,0,0,.25)}
.search svg{position:absolute;left:13px;top:8px}

/* tips strip */
.tipsbar{left:0;top:103px;width:1200px;height:44px;background:linear-gradient(#fafafa,#eaeaea);border-bottom:1px solid var(--line)}
.crumb{left:18px;top:13px;font-size:12.5px;color:#333}
.tip{left:348px;top:3px;width:677px;height:36px;background:var(--white);border:1px solid var(--line);border-radius:3px;display:flex;align-items:center;padding-left:12px;font-size:13px;gap:4px;white-space:nowrap}
.tip b{color:var(--blue);font-style:italic}
.tip .more{color:var(--blue);font-style:italic;font-weight:700;font-size:12px;margin-left:6px}
.tip .close{position:absolute;right:12px;top:11px}
.showtips{left:1077px;top:12px;display:flex;align-items:center;gap:6px;color:var(--blue);font-style:italic;font-weight:700;font-size:16px}
.check{width:16px;height:16px;border:1px solid #bbb;background:var(--white);border-radius:2px;display:flex;align-items:center;justify-content:center;flex:none}

/* sidebar */
.sidebar{left:0;top:147px;width:206px;height:623px;background:var(--white);border-right:1px solid var(--line)}
.sidebar-head{height:40px;background:linear-gradient(#f7f7f7,#e9e9e9);padding:12px 18px;font-weight:700;color:#444;font-size:14px;display:flex;justify-content:space-between}
.filters{list-style:none;padding:8px 18px}
.filters li{display:flex;align-items:center;gap:12px;height:28px;font-size:14px}
.filters .check{border-color:#ddd;background:#f7f7f7}
.cloud-title{left:17px;top:461px;font-weight:700;font-style:italic;font-size:20px;line-height:26px}
.cloud{left:14px;top:498px;width:186px;display:flex;flex-direction:column;gap:17px}
.cloud-row{display:flex;gap:4px;white-space:nowrap}
.tag{height:22px;padding:0 8px;border:1px solid #c8c8c8;border-radius:11px;background:var(--tag-bg);font-size:11.5px;line-height:20px;color:#333}
.tag.on{background:var(--blue);border-color:var(--blue-dark);color:var(--white)}
.addtag{left:16px;top:729px;width:174px;height:26px;border:1px solid #bbb;border-radius:13px;padding:4px 12px;font-size:12px;box-shadow:inset 0 1px 2px rgba(0,0,0,.15)}

/* message table */
.list{left:206px;top:147px;width:994px;height:446px;overflow:hidden}
.list-head{height:21px;background:linear-gradient(#fafafa,#e4e4e4);border-bottom:1px solid var(--line);font-weight:700;font-size:12px;display:grid;grid-template-columns:615px 66px 164px 132px}
.list-head div{padding:3px 10px;border-left:1px solid var(--line)}
.list-head div:first-child{border-left:0;padding-left:40px}
.row{display:grid;grid-template-columns:34px 581px 66px 164px 132px;border-bottom:1px solid var(--line);background:var(--row-alt);width:977px}
.row:nth-child(odd){background:var(--row)}
.row>div{display:flex;align-items:center}
.row .star{justify-content:center}
.row .subject{padding:0 6px;font-size:12.5px;line-height:16px}
.row .source,.row .tags,.row .date{border-left:1px solid var(--line)}
.row .source{justify-content:center}
.row .tags{padding:0 12px;font-size:12.5px;line-height:18px}
.row .date{padding:0 12px;font-size:13.5px}
.thumb{width:102px;height:76px;border:1px solid #bbb;margin-right:20px;flex:none}
.thumb.video{background:linear-gradient(#e8e8e8 0 18%,#2a2a2a 18% 62%,#f2f2f2 62%)}
.thumb.sport{background:linear-gradient(#f5f5f5 0 15%,#6c7480 15% 70%,#f2f2f2 70%)}
.url{color:var(--link)}
.scroll{left:1183px;top:168px;width:17px;height:425px;background:#eee;border-left:1px solid var(--line)}
.scroll-thumb{left:2px;top:6px;width:12px;height:128px;border-radius:6px;background:linear-gradient(90deg,var(--blue-light),var(--blue-dark))}

/* splitter + preview */
.splitter{left:206px;top:593px;width:994px;height:24px;background:linear-gradient(#fff,#e8e8e8);border-top:1px solid var(--line)}
.grip{left:535px;top:8px;width:42px;height:7px;border-top:1px solid #bbb;border-bottom:1px solid #bbb}
.preview-head{left:206px;top:617px;width:994px;height:71px;background:var(--preview-head)}
.source-badge{left:39px;top:17px;width:38px;height:38px;background:var(--white);border:1px solid #bbb;border-radius:3px;display:flex;align-items:center;justify-content:center}
.meta{left:89px;top:11px;font-size:12.5px;line-height:16px;display:grid;grid-template-columns:39px auto}
.meta dt{font-weight:700}
.fav{left:843px;top:14px;width:134px;height:42px;border-radius:3px;background:linear-gradient(var(--blue-light),var(--blue-dark));color:var(--white);font-weight:700;font-size:12px;display:flex;align-items:center;justify-content:center;gap:8px}
.fav .check{border-color:var(--white)}
.preview-body{left:248px;top:704px;width:930px;font-size:13.5px;line-height:19px}
.hashtag{color:var(--blue);font-style:italic;font-weight:700}
</style>
</head>
<body>

<header class="abs topbar">
  <div class="abs brand"><span class="brand-dot"></span><span class="brand-name">telvoqa.io</span></div>
  <div class="abs social"><span></span><span></span><span></span></div>
  <nav class="abs nav"><a>Home</a><a>About</a><a>Contact</a></nav>
  <div class="abs user"><span class="avatar" role="img" aria-label="User avatar"></span>User Name</div>
</header>

<div class="abs toolbar">
  <div class="abs tool" style="left:15px"><svg width="14" height="14"><path d="M12 1 L2 7 L12 13Z" fill="#1a3e5a"/></svg></div>
  <div class="abs tool" style="left:94px"><svg width="14" height="14"><path d="M2 1 L12 7 L2 13Z" fill="#1a3e5a"/></svg></div>
  <div class="abs tool" style="left:173px"><svg width="16" height="16"><path d="M13 8 A5 5 0 1 1 10.5 3.7" fill="none" stroke="#1a3e5a" stroke-width="2.4"/><path d="M9 1 L14 3 L10 7Z" fill="#1a3e5a"/></svg></div>
  <div class="abs tool" style="left:251px"><svg width="14" height="14"><path d="M2 2 L12 12 M12 2 L2 12" stroke="#1a3e5a" stroke-width="3"/></svg></div>
  <div class="abs search"><svg width="18" height="18"><circle cx="10" cy="7" r="5" fill="none" stroke="#999" stroke-width="2"/><path d="M6 11 L2 15" stroke="#999" stroke-width="2.5"/></svg></div>
</div>

<div class="abs tipsbar">
  <div class="abs crumb">Inbox - All - (15 messages)</div>
  <div class="abs tip">
    <svg width="12" height="18"><circle cx="6" cy="6" r="5.5" fill="#1f8fd3"/><rect x="3.5" y="11" width="5" height="5" fill="#1f8fd3"/></svg>
    <b>Tips:</b> Lorem ipsum dolor sit amet, consectetur adipisicing, dolor sit amet, consectetur adipisicing <span class="more">more tips &gt;</span>
    <svg class="close" width="12" height="12"><path d="M2 2 L10 10 M10 2 L2 10" stroke="#1d2d3a" stroke-width="2.5"/></svg>
  </div>
  <div class="abs showtips">
    <svg width="12" height="18"><circle cx="6" cy="6" r="5.5" fill="#1f8fd3"/><rect x="3.5" y="11" width="5" height="5" fill="#1f8fd3"/></svg>
    Show tips <span class="check"><svg width="12" height="10"><path d="M1 5 L4.5 8.5 L11 1" fill="none" stroke="#1f8fd3" stroke-width="2"/></svg></span>
  </div>
</div>

<aside class="abs sidebar">
  <div class="sidebar-head">INBOX <svg width="12" height="8" style="margin-top:4px"><path d="M0 0 H12 L6 7Z" fill="#666"/></svg></div>
  <ul class="filters">
    <li><span class="check"><svg width="12" height="10"><path d="M1 5 L4.5 8.5 L11 1" fill="none" stroke="#1f8fd3" stroke-width="2"/></svg></span>All Messages</li>
    <li><span class="check"></span>Peoplewallo</li>
    <li><span class="check"></span>Chirpnest</li>
    <li><span class="check"></span>Email</li>
    <li><span class="check"></span>SMS</li>
  </ul>
</aside>
<h2 class="abs cloud-title">Cloud Tag:</h2>
<div class="abs cloud">
  <div class="cloud-row"><span class="tag">cloud</span><span class="tag">finger</span><span class="tag">peoplewallo</span></div>
  <div class="cloud-row"><span class="tag">chirpnest</span><span class="tag on">family</span><span class="tag">danger</span></div>
  <div class="cloud-row"><span class="tag">Close</span><span class="tag">monochrome</span><span class="tag">Sad</span></div>
  <div class="cloud-row"><span class="tag">texture</span><span class="tag on">illustration</span><span class="tag">dave</span></div>
  <div class="cloud-row"><span class="tag">michael</span><span class="tag">Cute</span><span class="tag">handmade</span></div>
  <div class="cloud-row"><span class="tag">transparency</span><span class="tag">bright</span><span class="tag">tv</span></div>
</div>
<div class="abs addtag">add tag</div>

<section class="abs list">
  <div class="list-head"><div>Subject</div><div>Source</div><div>Tags</div><div>Date Received</div></div>

  <div class="row" style="height:75px">
    <div class="star"><svg width="16" height="16"><path d="M8 0.5 L10 6 L15.5 6 L11 9.5 L12.8 15 L8 11.7 L3.2 15 L5 9.5 L0.5 6 L6 6Z" fill="#1f8fd3"/></svg></div>
    <div class="subject"><p>Lorem ipsum dolor sit amet, consectetur adipisicing elit, sed do eiusmod tempor incididunt ut labore et dolore magna aliqua. Ut enim ad minim veniam, quis nostrud exercitation ullamco laboris nisi ut aliquip ex ea commodo consequat. ed do eiu aliquip enci.</p></div>
    <div class="source"><svg width="18" height="16"><ellipse cx="9" cy="7" rx="8" ry="6" fill="#4a5560"/><path d="M4 11 L3 15 L8 12Z" fill="#4a5560"/></svg></div>
    <div class="tags">coud, momochrome, Sad texture, handmade</div>
    <div class="date">5 mins ago</div>
  </div>

  <div class="row" style="height:97px">
    <div class="star"><svg width="16" height="16"><path d="M8 0.5 L10 6 L15.5 6 L11 9.5 L12.8 15 L8 11.7 L3.2 15 L5 9.5 L0.5 6 L6 6Z" fill="#c8c8c8"/></svg></div>
    <div class="subject"><span class="thumb video" role="img" aria-label="Thumbnail of the linked video page"></span><span class="url">http://www.clipverra.com/watch/jax-render/mirror-teaser/TIVEV1256262</span></div>
    <div class="source"><svg width="16" height="12"><rect width="16" height="12" fill="#4a5560"/><path d="M0 0 L8 7 L16 0" fill="none" stroke="#fff" stroke-width="1.3"/></svg></div>
    <div class="tags">streamholt, video, Mira Lanes, bright</div>
    <div class="date">January 27, 2012</div>
  </div>

  <div class="row" style="height:96px">
    <div class="star"><svg width="16" height="16"><path d="M8 0.5 L10 6 L15.5 6 L11 9.5 L12.8 15 L8 11.7 L3.2 15 L5 9.5 L0.5 6 L6 6Z" fill="#c8c8c8"/></svg></div>
    <div class="subject"><span class="thumb sport" role="img" aria-label="Thumbnail of the linked sports video page"></span><span class="url" style="margin-left:-5px">http://www.streamholt.com/watch?v=dQLCO9JkVeE&amp;feature=g-logo&amp;context<br>=G28a9c97FOAAAAAAAAAA</span></div>
    <div class="source"><svg width="16" height="12"><rect width="16" height="12" fill="#4a5560"/><path d="M0 0 L8 7 L16 0" fill="none" stroke="#fff" stroke-width="1.3"/></svg></div>
    <div class="tags">clipverra, video, Z-cup, sports</div>
    <div class="date">January 27, 2012</div>
  </div>

  <div class="row" style="height:54px">
    <div class="star"><svg width="16" height="16"><path d="M8 0.5 L10 6 L15.5 6 L11 9.5 L12.8 15 L8 11.7 L3.2 15 L5 9.5 L0.5 6 L6 6Z" fill="#c8c8c8"/></svg></div>
    <div class="subject"><p>Yesterday, Marlo Jumped the fence in my backyard and ran across my lawn singing "my father owns this". In my excite... <span class="url">http://snip.lo/dMG12po</span></p></div>
    <div class="source"><svg width="16" height="16"><circle cx="8" cy="8" r="7" fill="#4a5560"/></svg></div>
    <div class="tags">chirpnest, backyard</div>
    <div class="date">Yesterday</div>
  </div>

  <div class="row" style="height:92px">
    <div class="star"><svg width="16" height="16"><path d="M8 0.5 L10 6 L15.5 6 L11 9.5 L12.8 15 L8 11.7 L3.2 15 L5 9.5 L0.5 6 L6 6Z" fill="#c8c8c8"/></svg></div>
    <div class="subject"><span class="thumb video" role="img" aria-label="Thumbnail of the linked video page"></span><span class="url">http://www.clipverra.com/watch/jax-render/mirror-teaser/TIVEV1256262</span></div>
    <div class="source"><svg width="16" height="12"><rect width="16" height="12" fill="#4a5560"/><path d="M0 0 L8 7 L16 0" fill="none" stroke="#fff" stroke-width="1.3"/></svg></div>
    <div class="tags">clipverra, video, Z-cup, sports</div>
    <div class="date">January 27, 2012</div>
  </div>
</section>
<div class="abs scroll"><div class="abs scroll-thumb"></div></div>

<div class="abs splitter"><div class="abs grip"></div></div>

<div class="abs preview-head">
  <div class="abs source-badge"><svg width="20" height="20"><circle cx="10" cy="10" r="8" fill="#2a9fe0"/></svg></div>
  <dl class="abs meta">
    <dt>From:</dt><dd>name@email.com</dd>
    <dt>Date:</dt><dd>Today</dd>
    <dt>Tags</dt><dd>cloud, momochrome, sad, texture, handmade</dd>
  </dl>
  <div class="abs fav"><span class="check"><svg width="12" height="10"><path d="M1 5 L4.5 8.5 L11 1" fill="none" stroke="#1f8fd3" stroke-width="2"/></svg></span><svg width="16" height="16"><path d="M8 0.5 L10 6 L15.5 6 L11 9.5 L12.8 15 L8 11.7 L3.2 15 L5 9.5 L0.5 6 L6 6Z" fill="#fff"/></svg>FAVORITE</div>
</div>
<p class="abs preview-body">Lorem ipsum dolor sit amet, consectetur adipisicing elit, sed do eiusmod tempor incididunt ut labore et dolore magna aliqua. Ut enim ad minim veniam, quis nostrud exercitation ullamco laboris nisi ut aliquip ex ea commodo consequat. Duis aute irure dolor in reprehenderit in voluptate velit esse cillum <span class="hashtag">#urgent</span></p>

</body>
</html>
```